We sell companies excess stock for them

We need a business card for a company based in New Zealand called 'ShelfLark'.

Check out our website to get an idea www.shelflark.example

We help other businesses to;
- Sell Excess Stock
- Manage Product Returns
- Sell Company Assets

Our logo is attached for your reference
The font used is 'RifficFree-Bold'

Target Market(s)

Businesses

Industry/Entity Type

Business

Contact Information for Business Card

Name: Mara Quillby
Phone: 027 864 3190
email: maraquillby@shelflark.example
website: www.shelflark.example

Font styles to use
Other font styles liked:

Colors
9bcb3b

Requirements
Must have
Nice to have
Should not have

```html
<!DOCTYPE html>
<html lang="en">
<head>
<meta charset="utf-8">
<title>ShelfLark Business Card</title>
<link href="https://fonts.googleapis.com/css2?family=Fredoka:wght@600;700&family=Lato:wght@400;700&display=swap" rel="stylesheet">
<style>
  :root {
    --lime: #9bcb3b;
    --ink: #2b2626;
    --text: #333333;
    --paper: #ffffff;
    --stage: #1c1c1c;
    --card-dark: #262626;
    --card-dark-edge: #1f1f1f;
    --emboss: #4a4a4a;
    --mascot-a: #b8dc6e;
    --mascot-b: #f0a93c;
  }
  * { margin: 0; padding: 0; box-sizing: border-box; }
  html, body {
    width: 1200px; height: 897px; overflow: hidden;
    background: var(--stage);
  }
  .canvas { position: relative; width: 1200px; height: 897px; }

  .card {
    position: absolute; left: 304px; width: 594px; height: 338px;
    border-radius: 18px; overflow: hidden;
  }
  .card--front { top: 92px; background: var(--paper); }
  .card--back {
    top: 470px;
    background: radial-gradient(ellipse at 60% 55%, #333 0%, var(--card-dark) 45%, var(--card-dark-edge) 100%);
  }

  .brand {
    font-family: "Fredoka", sans-serif; font-weight: 700;
    color: var(--ink); letter-spacing: -0.5px; line-height: 1;
  }
  .card--front .brand { position: absolute; left: 40px; top: 36px; font-size: 48px; }

  .mascot-area {
    position: absolute; left: 392px; top: 26px; width: 160px; height: 172px;
    border-radius: 40% 45% 38% 42%;
    background: radial-gradient(circle at 45% 40%, var(--mascot-a) 0%, #d6c06a 55%, var(--mascot-b) 100%);
    opacity: 0.85;
  }

  .person { position: absolute; left: 41px; top: 155px; }
  .person__name {
    font-family: "Fredoka", sans-serif; font-weight: 700; font-size: 23px;
    color: var(--ink); line-height: 1; letter-spacing: 0.3px;
  }
  .person__name .accent { color: var(--lime); }
  .person__role { font-family: "Lato", sans-serif; font-size: 15px; color: var(--text); margin-top: 6px; }

  .divider { position: absolute; left: 39px; top: 218px; width: 515px; height: 2px; background: var(--lime); }

  .contacts { position: absolute; left: 41px; top: 237px; list-style: none;
    font-family: "Lato", sans-serif; font-size: 15px; color: var(--text); }
  .contacts li { display: flex; align-items: center; height: 19.5px; }
  .contacts svg { width: 12px; height: 12px; margin-right: 11px; fill: var(--lime); }
  .contacts .accent { color: var(--lime); }

  .services { position: absolute; right: 40px; top: 236px; text-align: right;
    font-family: "Lato", sans-serif; font-size: 15px; color: var(--text); line-height: 19.5px; }
  .services__lead { font-family: "Fredoka", sans-serif; font-weight: 700; color: var(--lime); font-size: 15px; }

  .footer-band { position: absolute; left: 0; bottom: 0; width: 594px; height: 30px; }

  .card--back .brand {
    position: absolute; left: 0; right: 0; top: 138px; text-align: center;
    font-size: 64px; color: var(--emboss);
  }
  .back-url {
    position: absolute; left: 0; right: 0; top: 296px; text-align: center;
    font-family: "Lato", sans-serif; font-size: 15px; letter-spacing: 1.8px; color: #e6e6e6;
  }
  .back-url .accent { color: var(--lime); }
</style>
</head>
<body>
<div class="canvas">

  <section class="card card--front">
    <div class="brand">ShelfLark</div>
    <div class="mascot-area" role="img" aria-label="Cartoon mascot courier in a green cap carrying an orange parcel and giving a thumbs up"></div>

    <div class="person">
      <div class="person__name">MARA <span class="accent">QUILLBY</span></div>
      <div class="person__role">Director</div>
    </div>

    <div class="divider"></div>

    <ul class="contacts">
      <li><svg viewBox="0 0 24 24"><path d="M6.6 10.8a15 15 0 0 0 6.6 6.6l2.2-2.2c.3-.3.7-.4 1-.2 1.1.4 2.3.6 3.6.6.6 0 1 .4 1 1V20c0 .6-.4 1-1 1A17 17 0 0 1 3 4c0-.6.4-1 1-1h3.5c.6 0 1 .4 1 1 0 1.3.2 2.5.6 3.6.1.3 0 .7-.2 1z"/></svg>027 864 3190</li>
      <li><svg viewBox="0 0 24 24"><path d="M2 5h20v14H2z M2 5l10 8 10-8" stroke="#fff" stroke-width="1.5"/></svg>maraquillby@shelflark.example</li>
      <li><svg viewBox="0 0 24 24"><path d="M12 2a10 10 0 1 0 0 20 10 10 0 0 0 0-20zm0 2c.9 1.2 1.6 2.6 2 4h-4c.4-1.4 1.1-2.8 2-4zM4.3 14a8 8 0 0 1 0-4h3.4a16 16 0 0 0 0 4zm.9 2h3c.3 1.3.8 2.5 1.4 3.6A8 8 0 0 1 5.2 16zm3-8h-3a8 8 0 0 1 4.4-3.6C8.9 5.5 8.5 6.7 8.2 8zM12 20c-.9-1.2-1.6-2.6-2-4h4c-.4 1.4-1.1 2.8-2 4zm2.3-6H9.7a14 14 0 0 1 0-4h4.6a14 14 0 0 1 0 4zm.1 5.6c.6-1.1 1.1-2.3 1.4-3.6h3a8 8 0 0 1-4.4 3.6zM16.3 14a16 16 0 0 0 0-4h3.4a8 8 0 0 1 0 4zm-.5-6c-.3-1.3-.8-2.5-1.4-3.6A8 8 0 0 1 18.8 8z"/></svg>www.<span class="accent">shelflark</span>.example</li>
    </ul>

    <div class="services">
      <div class="services__lead">We help other businesses to:</div>
      <div>Sell Excess Stock</div>
      <div>Manage Product Returns</div>
      <div>Sell Company Assets</div>
    </div>

    <svg class="footer-band" viewBox="0 0 594 30" preserveAspectRatio="none" aria-hidden="true">
      <path d="M250 10 C 270 10, 280 18, 300 18 L 594 18 L 594 14 L 300 14 C 285 14, 275 10, 250 10 Z" fill="#2b2626"/>
      <path d="M0 5 L 215 5 C 245 5, 255 20, 290 20 L 594 20 L 594 30 L 0 30 Z" fill="#9bcb3b"/>
    </svg>
  </section>

  <section class="card card--back">
    <div class="brand">ShelfLark</div>
    <div class="back-url">www.<span class="accent">shelflark</span>.example</div>
  </section>

</div>
</body>
</html>
```